Forge Kinetic Apex label design for two sports nutrition powders

We need a Label designed done for 2 Products .

1 is a Pre Workout Powder - product name
"Volcor Apex "
2 Is a BCAA Powder product name "Restra Apex "

Please see attached our Brand Logo and I have added some concepts of other brand I would like to use as a base Look .

Black Matt Background is key and the use of Red like examples

Target Market(s)

Sports Nutrition Market

Industry/Entity Type

Nutrition

Font styles to use
Sans Serif

Requirements
Must have
• As per sample packaging I sent we need to make sure its the matt background and label is sharpe
Nice to have
• Very cool label
Should not have
• Open to most things

```html
<!DOCTYPE html>
<html lang="en">
<head>
<meta charset="utf-8">
<title>Forge Kinetic Apex – Volcor Apex &amp; Restra Apex Labels</title>
<link rel="stylesheet" href="https://fonts.googleapis.com/css2?family=Open+Sans:ital,wght@1,700&family=Roboto+Condensed:wght@700&family=Mr+Dafoe&display=swap">
<style>
  :root {
    --page-bg: #e6f7f7;
    --label-black: #0c0c0e;
    --brand-red: #e8303e;
    --script-red: #e3202c;
    --pre-yellow: #f5bd12;
    --bcaa-blue: #12b2ec;
    --silver-light: #e9e9eb;
    --silver-mid: #b9bbbf;
    --silver-dark: #7a7d82;
    --white: #ffffff;
  }
  * { margin: 0; padding: 0; box-sizing: border-box; }
  html, body {
    width: 1040px;
    height: 1200px;
    overflow: hidden;
    background: var(--page-bg);
  }
  .canvas {
    position: relative;
    width: 1040px;
    height: 1200px;
    display: flex;
    justify-content: center;
    align-items: center;
    gap: 40px;
  }
  .label {
    position: relative;
    width: 480px;
    height: 560px;
    background: var(--label-black);
    overflow: hidden;
  }
  .mascot-art {
    position: absolute;
    left: 6px;
    top: 70px;
    width: 240px;
    height: 290px;
    border-radius: 46% 40% 50% 40%;
    background: radial-gradient(ellipse at 55% 35%, var(--silver-mid) 0%, var(--silver-dark) 40%, rgba(40,40,44,0.9) 75%, var(--label-black) 100%);
  }
  .category-band {
    position: absolute;
    left: 190px;
    right: 0;
    top: 122px;
    height: 34px;
    padding-right: 18px;
    display: flex;
    align-items: center;
    justify-content: flex-end;
    font-family: "Open Sans", sans-serif;
    font-style: italic;
    font-weight: 700;
    font-size: 21px;
    color: var(--white);
  }
  .label--pre .category-band { background: var(--brand-red); }
  .label--bcaa .category-band { background: var(--bcaa-blue); }
  .product-name {
    position: absolute;
    right: 22px;
    top: 150px;
    font-family: "Roboto Condensed", sans-serif;
    font-weight: 700;
    font-size: 76px;
    line-height: 1;
    letter-spacing: -1px;
    color: var(--silver-light);
  }
  .product-script {
    position: absolute;
    left: 250px;
    top: 208px;
    font-family: "Mr Dafoe", cursive;
    font-size: 104px;
    line-height: 1;
    color: var(--script-red);
    transform: rotate(-10deg);
  }
  .wave-bands {
    position: absolute;
    left: 0;
    bottom: 0;
    width: 480px;
    height: 220px;
  }
  .brand-mark {
    position: absolute;
    left: 26px;
    top: 404px;
    display: flex;
    align-items: center;
    gap: 8px;
  }
  .brand-mark__dot {
    width: 20px;
    height: 20px;
    border-radius: 50%;
    background: var(--brand-red);
  }
  .brand-mark__name {
    font-family: "Roboto Condensed", sans-serif;
    font-weight: 700;
    font-size: 22px;
    letter-spacing: 0.5px;
    color: var(--label-black);
  }
</style>
</head>
<body>
<main class="canvas">

  <section class="label label--pre">
    <div class="mascot-art" role="img" aria-label="Silver roaring bear mascot illustration with claw marks"></div>
    <div class="category-band">Pre Workout Powder</div>
    <div class="product-name">Volcor</div>
    <div class="product-script">Apex</div>
    <svg class="wave-bands" viewBox="0 0 480 220" aria-hidden="true">
      <path d="M0 30 L300 30 C360 30 400 0 480 10 L480 60 C400 50 340 80 280 80 L0 80 Z" fill="var(--pre-yellow)"/>
      <path d="M300 48 C370 40 420 20 480 30 L480 55 C420 45 370 70 290 74 Z" fill="#7cc242"/>
      <path d="M0 80 L280 80 C340 80 400 50 480 60 L480 80 C400 72 340 110 270 110 L0 110 Z" fill="var(--silver-mid)"/>
      <path d="M0 110 L270 110 C340 110 400 76 480 82 L480 200 C420 205 380 212 240 212 L0 205 Z" fill="var(--brand-red)"/>
    </svg>
    <div class="brand-mark">
      <span class="brand-mark__dot"></span>
      <span class="brand-mark__name">FORGE KINETIC APEX</span>
    </div>
  </section>

  <section class="label label--bcaa">
    <div class="mascot-art" role="img" aria-label="Silver roaring bear mascot illustration with claw marks"></div>
    <div class="category-band">BCAA Powder</div>
    <div class="product-name">Restra</div>
    <div class="product-script">Apex</div>
    <svg class="wave-bands" viewBox="0 0 480 220" aria-hidden="true">
      <path d="M0 40 L300 40 C360 40 400 5 480 12 L480 55 C400 48 340 84 280 84 L0 84 Z" fill="var(--bcaa-blue)"/>
      <path d="M0 84 L280 84 C340 84 400 54 480 60 L480 82 C400 74 340 112 270 112 L0 112 Z" fill="var(--silver-mid)"/>
      <path d="M0 112 L270 112 C340 112 400 78 480 84 L480 200 C420 205 380 212 240 212 L0 205 Z" fill="var(--brand-red)"/>
    </svg>
    <div class="brand-mark">
      <span class="brand-mark__dot"></span>
      <span class="brand-mark__name">FORGE KINETIC APEX</span>
    </div>
  </section>

</main>
</body>
</html>
```